ALL TEXT GRAPHICS TM May 2025 for Instagram

We are looking for a series of social media graphics for Instagram (new size: 4:5 (1080 x 1350 pixels) ratio that are ALL TEXT. We want the following quotes below on each graphic; one quote per graphic. AND, In very small letters at the bottom of each graphic, add @TovaMarshOnline
The look and feel of these graphics should be complimentary to the color palette attached below; but keep them simple. But the design is up to you; at the end of this document, I provided various samples of all text graphics that I like as examples.
Target Market(s)
women looking to lose weight
Look and feel

```html
<!DOCTYPE html>
<html lang="en">
<head>
<meta charset="utf-8">
<title>Hormone Series – Instagram Text Graphics</title>
<link href="https://fonts.googleapis.com/css2?family=Fraunces:ital,opsz,wght@1,9..144,900&family=Mali:wght@600;700&display=swap" rel="stylesheet">
<style>
  :root {
    --board-grey: #c6c6c6;
    --magenta-deep: #cc0066;
    --magenta-light: #ff99ff;
    --bubble-pink: #ff66ad;
    --hot-pink: #ff0880;
    --quote-rose: #c8086a;
    --white: #ffffff;
    --ink: #000000;
  }
  * { margin: 0; padding: 0; box-sizing: border-box; }
  html, body { width: 982px; height: 1200px; overflow: hidden; }
  body {
    background: var(--board-grey);
    position: relative;
    font-family: "Mali", "Comic Sans MS", cursive;
  }
  .post {
    position: absolute;
    width: 406px;
    height: 507px;
    overflow: hidden;
  }
  .post-shape { position: absolute; inset: 0; width: 100%; height: 100%; }
  .headline {
    position: absolute;
    left: 0; right: 0;
    text-align: center;
    font-family: "Fraunces", Georgia, serif;
    font-style: italic;
    font-weight: 900;
    letter-spacing: -0.5px;
    white-space: nowrap;
  }
  .body-copy {
    position: absolute;
    text-align: center;
    color: var(--ink);
    font-weight: 700;
    font-size: 25px;
    line-height: 27px;
    white-space: nowrap;
  }
  .body-copy p + p { margin-top: 27px; }

  /* Post 1 */
  .post--tired {
    left: 72px; top: 78px;
    background: linear-gradient(to bottom, var(--magenta-deep), var(--magenta-light));
  }
  .post--tired .headline {
    top: 40px; color: var(--white);
    font-size: 30px; line-height: 34px;
  }
  .post--tired .body-copy { left: 93px; width: 217px; top: 213px; }

  /* Post 2 */
  .post--fault { left: 508px; top: 76px; background: var(--white); }
  .post--fault .headline {
    top: 23px; color: var(--white);
    font-size: 32px; line-height: 38px;
  }
  .post--fault .body-copy { left: 0; right: 0; top: 300px; }

  /* Post 3 */
  .post--belly { left: 289px; top: 615px; background: var(--white); }
  .post--belly .headline {
    top: 55px; left: 28px; right: auto; width: 264px; color: var(--ink);
    font-size: 34px; line-height: 37px;
  }
  .post--belly .body-copy {
    left: 40px; width: 256px; top: 188px;
    font-size: 29px; line-height: 33px;
  }
  .post--belly .body-copy p + p { margin-top: 33px; }
</style>
</head>
<body>

  <section class="post post--tired">
    <svg class="post-shape" viewBox="0 0 406 507" aria-hidden="true">
      <rect x="93" y="173" width="217" height="286" rx="26" fill="var(--white)"/>
      <rect x="103" y="183" width="197" height="266" rx="20" fill="none" stroke="var(--quote-rose)" stroke-width="2.5"/>
      <rect x="130" y="170" width="42" height="26" fill="var(--white)"/>
      <text x="151" y="205" text-anchor="middle" font-family="Georgia, serif" font-weight="700" font-size="48" fill="var(--quote-rose)">“</text>
      <rect x="231" y="436" width="42" height="26" fill="var(--white)"/>
      <text x="252" y="471" text-anchor="middle" font-family="Georgia, serif" font-weight="700" font-size="48" fill="var(--quote-rose)">”</text>
    </svg>
    <h2 class="headline">Tired. Moody.<br>Stubborn<br>Belly Fat.</h2>
    <div class="body-copy">
      <p>Your<br>hormones<br>are<br>screaming<br>for help!</p>
      <p>Let’s fix<br>that.</p>
    </div>
  </section>

  <section class="post post--fault">
    <svg class="post-shape" viewBox="0 0 718 897" preserveAspectRatio="none" aria-hidden="true">
      <path d="M0 0 H718 V272 C610 360 470 400 393 400 C393 450 415 485 454 513 C385 490 325 450 286 398 C170 385 70 335 0 275 Z" fill="var(--bubble-pink)"/>
    </svg>
    <h2 class="headline">That stubborn<br>weight?<br>It’s not your<br>fault.</h2>
    <div class="body-copy">
      <p>Your hormones<br>are to blame<br>and you’re not<br>alone;</p>
      <p>But there is a<br>fix.</p>
    </div>
  </section>

  <section class="post post--belly">
    <svg class="post-shape" viewBox="0 0 406 507" aria-hidden="true">
      <rect x="264" y="0" width="142" height="507" fill="var(--hot-pink)"/>
      <path d="M256 54 H287 Q295 54 295 62 V229 L311 247 L295 265 V453 Q295 461 287 461 H256 Z" fill="var(--white)"/>
    </svg>
    <h2 class="headline">Your belly<br>isn’t fat… it’s<br>hormonal.</h2>
    <div class="body-copy">
      <p>And here’s how<br>to fix it.</p>
      <p>Comment</p>
      <p>HORMONES<br>if nothing is<br>working.</p>
    </div>
  </section>

</body>
</html>
```